Poster for a new "Pizza Roll" Combo at our bakery

We are a cinnamon roll and coffee focused bakery, but we would like an innovative poster design to bring attention to our new offering, a Pizza Roll. We will be offering it as a combo, and this is what we wish to advertise. It will be geared mainly towards a younger high school aged crowd. I have included pics of the Pizza Rolls, but it's up to you how you want to incorporate them in the design.Poster should include our logo, the pizza rolls, and can include a drink to illustrate the combo as well. ( we offer710 ml vima bottle products and lurn bottled waters)Main Text: Try our amazing new Pizza Rolls! Message to get accross: $6.00 for a Pizza Roll and drink.Small Print: Avail after 11am, while supplies last. Includes one pizza roll and one bottled drink of choice. Taxes extra.

Target Market(s)

Broad, but mainly high school aged kids

Industry/Entity Type

Bakery

Colors

Designer to choose colors to be used in the design.

Requirements
Must have
• Text: " Try our amazing new PIzza Rolls!:
• $6 Pizza Roll Combo (Pizza Roll and a drink)
Nice to have
• Pic of the PIzza Roll (photo shopped if needed to improve esthetics)
• Pic of a Bottled 710ml vima drink
Should not have
• Any animal product references, as we are a Vegan shop.

```html
<!DOCTYPE html>
<html lang="en">
<head>
<meta charset="utf-8">
<title>Pizza Roll Combo Poster</title>
<link rel="stylesheet" href="https://fonts.googleapis.com/css2?family=Bebas+Neue&family=Montserrat:wght@400;800;900&display=swap">
<style>
  :root {
    --ink: #252223;
    --purple: #6e5a9c;
    --yellow: #f5b335;
    --white: #ffffff;
    --black: #111010;
  }
  html, body { margin: 0; padding: 0; overflow: hidden; background: var(--ink); }
  .poster {
    position: relative; width: 800px; height: 1200px; overflow: hidden;
    background: var(--ink); font-family: "Montserrat", sans-serif; color: var(--white);
  }
  .poster > svg.shapes { position: absolute; inset: 0; }
  .ribbon-text {
    position: absolute; left: 246px; top: 64px; margin: 0;
    font-weight: 900; font-size: 36px; letter-spacing: 0.5px; line-height: 48px;
  }
  .combo-badge {
    position: absolute; left: 502px; top: 198px; width: 160px; margin: 0;
    font-family: "Bebas Neue", sans-serif; color: var(--white);
    font-size: 41px; line-height: 31px; text-align: center;
  }
  .price-tag {
    position: absolute; left: 488px; top: 286px; width: 190px; height: 78px;
    background: var(--purple); transform: rotate(5deg);
    display: flex; align-items: center; justify-content: center;
    font-family: "Bebas Neue", sans-serif; font-size: 54px; color: var(--white);
  }
  .headline { position: absolute; left: 0; top: 536px; width: 800px; margin: 0; text-align: center; }
  .headline-intro {
    display: block; font-weight: 400; font-size: 50px; line-height: 60px; letter-spacing: 4px;
  }
  .headline-pizza {
    display: block; margin-top: 20px; font-weight: 900; font-size: 108px; line-height: 108px;
    letter-spacing: 5px; color: var(--yellow);
  }
  .headline-rolls {
    display: block; margin-top: -12px; font-weight: 900; font-size: 130px; line-height: 130px;
    color: var(--purple); letter-spacing: 0;
  }
  .fine-print {
    position: absolute; left: 0; top: 920px; width: 800px; margin: 0; text-align: center;
    font-size: 21.5px; line-height: 30.5px;
  }
  .brand-name {
    position: absolute; left: 70px; top: 1102px; width: 120px; margin: 0; text-align: center;
    font-weight: 800; font-size: 17px; color: var(--white);
  }
  .web-address {
    position: absolute; left: 442px; top: 1120px; margin: 0;
    font-size: 22px; letter-spacing: 4px; color: var(--white);
  }
</style>
</head>
<body>
<div class="poster">
  <svg class="shapes" width="800" height="1200" viewBox="0 0 800 1200">
    <defs>
      <linearGradient id="drink-tone" x1="0" x2="0" y1="0" y2="1">
        <stop offset="0" stop-color="#c9c9c9"/>
        <stop offset="0.3" stop-color="#9e1a20"/>
        <stop offset="1" stop-color="#c21f27"/>
      </linearGradient>
      <radialGradient id="roll-tone" cx="0.5" cy="0.4" r="0.6">
        <stop offset="0" stop-color="#d9904a"/>
        <stop offset="0.6" stop-color="#e4c7a0"/>
        <stop offset="1" stop-color="#cbb59a"/>
      </radialGradient>
    </defs>

    <!-- combo photo areas -->
    <rect class="drink-photo" role="img" aria-label="Photo of a chilled bottled soft drink"
          x="134" y="30" width="146" height="504" rx="36" fill="url(#drink-tone)"/>
    <ellipse class="roll-photo" role="img" aria-label="Photo of a baked pizza roll with tomato swirl"
             cx="423" cy="410" rx="141" ry="120" fill="url(#roll-tone)"/>

    <!-- special offer ribbon -->
    <polygon class="ribbon" fill="var(--purple)" points="232,56 622,56 596,89 622,122 232,122"/>

    <!-- combo badge -->
    <circle class="badge-circle" cx="582" cy="226" r="77" fill="var(--yellow)"/>

    <!-- headline rules -->
    <g class="headline-rules" stroke="var(--purple)" stroke-width="1.5">
      <line x1="130" y1="710" x2="210" y2="710"/>
      <line x1="130" y1="728" x2="210" y2="728"/>
      <line x1="130" y1="746" x2="210" y2="746"/>
      <line x1="614" y1="710" x2="694" y2="710"/>
      <line x1="614" y1="728" x2="694" y2="728"/>
      <line x1="614" y1="746" x2="694" y2="746"/>
    </g>

    <!-- footer -->
    <polygon class="footer-band" fill="var(--purple)" points="0,1152 800,1012 800,1200 0,1200"/>
    <polygon class="brand-plate" fill="var(--yellow)" points="8,1068 124,1032 254,1068 254,1200 8,1200"/>
    <circle class="brand-circle" cx="130" cy="1114" r="60" fill="var(--black)"/>
    <g class="social-dots" fill="none" stroke="var(--white)" stroke-width="3">
      <circle cx="627" cy="1080" r="16"/>
      <circle cx="689" cy="1080" r="16"/>
      <circle cx="753" cy="1080" r="16"/>
    </g>
  </svg>

  <p class="ribbon-text">SPECIAL OFFER</p>
  <p class="combo-badge">PIZZA ROLL<br>&amp; DRINK</p>
  <div class="price-tag">ONLY $6</div>

  <h1 class="headline">
    <span class="headline-intro">TRY OUR<br>AMAZING NEW</span>
    <span class="headline-pizza">PIZZA</span>
    <span class="headline-rolls">ROLLS!</span>
  </h1>

  <p class="fine-print">Available after 11am, while supplies last.<br>Includes one pizza roll and one bottled drink of choice.<br>Taxes extra.</p>

  <p class="brand-name">Swirlhouse</p>
  <p class="web-address">www.swirlhouse.com</p>
</div>
</body>
</html>
```